Events Company Brochure Design Project

You are designing a brochure for events company based in Melbourne called Tidewell Events that produces mostly experiential events, like product launches, car unveilings, but also some fundraising, staff loyalty events etc. The company's clients are corporates, so it needs to have a slick/ clean design. we have a 14 page brochure we've marked up in word, so will provide all contents and images but are really looking for a layout. Company's visual identity is blue colour brushed steel background. The final design should communicate professionalism and creativity.
Target Market(s)
Marketing managers, training and development managers of corporate clients
Industry/Entity Type
Events
Look and feel

```html
<!DOCTYPE html>
<html lang="en">
<head>
<meta charset="utf-8">
<title>Tidewell Events – Brochure Cover Options</title>
<link href="https://fonts.googleapis.com/css2?family=Open+Sans:wght@600;700;800&display=swap" rel="stylesheet">
<style>
  :root {
    --page-bg: #ffffff;
    --navy: #1c2b5f;
    --steel-light: #e4e4e6;
    --steel-mid: #c9cacd;
    --steel-dark: #a9abaf;
    --steel-grain: rgba(255,255,255,0.35);
    --steel-grain-dark: rgba(120,122,128,0.18);
    --track-grey: #8d8f93;
    --track-dark: #5f6266;
    --car-red: #c7393a;
    --ghost-white: rgba(255,255,255,0.4);
  }
  * { margin: 0; padding: 0; box-sizing: border-box; }
  html, body { width: 1200px; height: 900px; overflow: hidden; background: var(--page-bg); }
  body { position: relative; font-family: "Open Sans", Arial, sans-serif; }

  .cover {
    position: absolute;
    top: 210px;
    width: 339px;
    height: 480px;
    overflow: hidden;
    background:
      repeating-linear-gradient(90deg, var(--steel-grain) 0 1px, transparent 1px 3px, var(--steel-grain-dark) 3px 4px, transparent 4px 7px),
      repeating-linear-gradient(90deg, transparent 0 11px, rgba(255,255,255,0.25) 11px 12px, transparent 12px 19px),
      linear-gradient(180deg, var(--steel-light) 0%, var(--steel-mid) 60%, var(--steel-dark) 100%);
  }
  .cover--a { left: 36px; }
  .cover--b { left: 430px; }
  .cover--c { left: 824px; }

  .brand {
    position: absolute;
    display: flex;
    align-items: center;
    color: var(--navy);
    font-weight: 800;
    line-height: 1;
    white-space: nowrap;
  }
  .brand__dot { border-radius: 50%; background: var(--navy); flex: none; }
  .cover--a .brand { left: 32px; top: 30px; font-size: 27px; gap: 10px; }
  .cover--a .brand__dot { width: 34px; height: 34px; }
  .cover--b .brand { left: 30px; top: 36px; font-size: 13.5px; gap: 6px; }
  .cover--b .brand__dot { width: 17px; height: 17px; }
  .cover--c .brand { left: 108px; top: 40px; font-size: 19px; gap: 8px; }
  .cover--c .brand__dot { width: 24px; height: 24px; }

  .tagline {
    position: absolute;
    color: var(--navy);
    font-weight: 600;
    text-transform: uppercase;
    letter-spacing: 0.06em;
    white-space: nowrap;
  }
  .cover--a .tagline { left: 34px; top: 98px; font-size: 15px; line-height: 21px; }
  .cover--b .tagline { left: 33px; top: 271px; font-size: 12.5px; line-height: 17px; }
  .cover--c .tagline { left: 31px; top: 136px; font-size: 14.5px; line-height: 22px; }

  .race-photo {
    position: absolute;
    left: 0;
    width: 100%;
    background:
      radial-gradient(ellipse 28% 30% at 50% 62%, var(--car-red) 0%, rgba(199,57,58,0.35) 55%, transparent 75%),
      linear-gradient(180deg, #7d7a72 0%, #9a9892 30%, var(--track-grey) 45%, #b0b1b3 75%, var(--track-dark) 100%);
  }
  .cover--a .race-photo, .cover--b .race-photo { top: 320px; height: 160px; }
  .cover--c .race-photo { top: 270px; height: 152px; }

  .vertical-name {
    position: absolute;
    left: 238px;
    top: 12px;
    height: 456px;
    writing-mode: vertical-rl;
    transform: rotate(180deg);
    color: var(--ghost-white);
    font-weight: 800;
    font-size: 40px;
    line-height: 1;
    white-space: nowrap;
  }
</style>
</head>
<body>
  <section class="cover cover--a">
    <div class="brand"><span class="brand__dot"></span>Tidewell Events</div>
    <p class="tagline">Partnerships<br>and professional<br>events</p>
    <div class="race-photo" role="img" aria-label="Photo of a red and white open-wheel race car speeding along a track"></div>
  </section>

  <section class="cover cover--b">
    <div class="brand"><span class="brand__dot"></span>Tidewell Events</div>
    <div class="race-photo" role="img" aria-label="Photo of a red and white open-wheel race car speeding along a track"></div>
    <p class="tagline">Partnerships<br>and professional events</p>
    <div class="vertical-name" aria-hidden="true">TIDEWELL EVENTS</div>
  </section>

  <section class="cover cover--c">
    <div class="brand"><span class="brand__dot"></span>Tidewell Events</div>
    <p class="tagline">Partnerships<br>and professional events</p>
    <div class="race-photo" role="img" aria-label="Photo of a red and white open-wheel race car speeding along a track"></div>
  </section>
</body>
</html>
```